tavrenimports.com

I had a logo designed by pixel harbor, and now need a website. I would like all the normal features a website would need.
Payment method etc and I'd like to be able to upload pictures

Target Market(s)

Parents, gift ideas, baby shower, online shopping

Industry/Entity Type

Crowd

Coding

Coded - Design and coding required

Number of Pages Required

1 page

Requirements
Must have
• Would like it to be accessible using a mobile phone
• must be given DNS code so i can add pages as needed
• must be able to upload pictures of products, and up date as needed
Nice to have
• additional pages with no content

```html
<!DOCTYPE html>
<html lang="en">
<head>
<meta charset="utf-8">
<title>Tavren — Children's Clothing</title>
<link href="https://fonts.googleapis.com/css2?family=Roboto:wght@300;400;500;700&display=swap" rel="stylesheet">
<style>
:root{
  --backdrop:#ececec;
  --page:#ffffff;
  --navy:#0d1440;
  --pink:#e8457a;
  --pink-soft:#f07aa0;
  --ink:#222;
  --muted:#666;
  --caption:#dcdcdc;
  --dark:#262626;
  --darker:#1c1c1c;
  --band:#3b3b3b;
  --line:#e6c9d4;
}
*{box-sizing:border-box;margin:0;padding:0}
html,body{width:1200px;height:3125px;overflow:hidden}
body{background:var(--backdrop);font-family:"Roboto",Arial,sans-serif;color:var(--ink);position:relative}
.page{position:absolute;left:100px;top:67px;width:996px;height:2989px;background:var(--page);box-shadow:0 4px 18px rgba(0,0,0,.18);overflow:hidden}
.abs{position:absolute}

/* top bar */
.topbar{left:0;top:0;width:996px;height:25px;background:var(--darker);display:flex;align-items:center;justify-content:space-between;padding:0 52px 0 58px}
.pay-mini{display:flex;gap:5px}
.pay-mini span{width:20px;height:11px;background:#5a6b9a;border-radius:2px}
.pay-mini span:nth-child(2){background:#8a8fb5}
.pay-mini span:nth-child(3){background:#c75a4c}
.account{display:flex;gap:22px;font-size:9px;color:#cfcfcf}
.account span::before{content:"";display:inline-block;width:6px;height:6px;border-radius:50%;background:#999;margin-right:5px}

/* header */
.header{left:0;top:25px;width:996px;height:106px}
.phone{left:60px;top:36px;display:flex;align-items:center;gap:12px;font-size:17px;color:#333}
.phone-ico{width:20px;height:20px;background:var(--pink-soft);border-radius:3px;display:flex;align-items:center;justify-content:center}
.brand{left:0;width:996px;top:24px;text-align:center;font-size:40px;font-weight:300;color:var(--navy);letter-spacing:1px}
.cart{left:884px;top:30px;width:48px;height:46px;background:var(--pink-soft);display:flex;align-items:center;justify-content:center}
.cart-count{left:900px;top:16px;width:18px;height:18px;border-radius:50%;background:var(--navy);color:#fff;font-size:10px;display:flex;align-items:center;justify-content:center}

/* nav */
.nav{left:0;top:131px;width:996px;height:46px;background:var(--navy);display:flex;align-items:center;padding-left:102px}
.nav a{color:#fff;text-decoration:none;font-size:11.5px;margin-right:28px;text-transform:uppercase}
.nav a.active{color:var(--pink-soft)}
.search{left:906px;top:143px}

/* hero */
.hero{left:0;top:177px;width:996px;height:321px;background:linear-gradient(90deg,#d9cfc9 0%,#efe9e6 30%,#e9e2df 55%,#dcd3cf 80%,#cfc6c2 100%)}

/* section titles */
.section-title{left:0;width:996px;text-align:center;font-size:21px;font-weight:400;color:var(--navy);text-transform:uppercase}
.rule{height:1px;background:var(--line)}

/* products */
.card{width:208px;height:217px;background:var(--caption)}
.card .photo{width:208px;height:142px}
.card .caption{padding:14px 16px;font-size:12px;color:#444;text-transform:uppercase}
.card .price{color:var(--pink);font-weight:700;font-size:12px;margin-top:3px}
.card.shop .caption{background:#0b0b0b;color:#fff;height:75px;position:relative}
.card.shop .arrow{position:absolute;right:16px;top:22px;width:26px;height:26px;border:1px solid #fff;display:flex;align-items:center;justify-content:center}
.shop-label{position:absolute;left:0;top:72px;width:208px;text-align:center;color:#fff;font-weight:700;font-size:15px}

/* promo */
.promo-left{left:75px;top:1168px;width:208px;height:215px;background:linear-gradient(135deg,#c9607a,#e8b7a8 50,#7f8ab0)}
.offer{position:absolute;left:18px;bottom:6px;width:172px;height:62px;background:rgba(220,220,220,.85);text-align:center;font-size:12px;color:#222;padding-top:8px;line-height:1.2}
.offer b{display:block;margin:6px auto 0;width:100px;background:var(--pink);color:#fff;font-size:9px;padding:3px 0}
.promo-center{left:296px;top:1168px;width:425px;height:215px;background:linear-gradient(90deg,#4a4a4a,#6f6a66 50%,#4a4a4a)}
.promo-center span{position:absolute;left:0;width:425px;top:118px;text-align:center;color:#fff;font-size:44px;font-weight:300;letter-spacing:-1px}
.promo-r1{left:729px;top:1168px;width:208px;height:101px;background:linear-gradient(90deg,#2e2d2f,#6b6a6e,#3a393c)}
.promo-r2{left:729px;top:1281px;width:208px;height:102px;background:linear-gradient(180deg,#a9c3d8,#c9c0b3 60%,#8f8578)}

/* news */
.news{left:0;top:1433px;width:996px;height:604px;background:linear-gradient(120deg,#5a5a5a,#4a4a4a 40%,#555 70%,#4c4a4e)}
.news-title{color:#fff}
.frame{border:2px solid #fff;background:#fff}
.news-h{font-size:15px;font-weight:700;color:#fff;text-transform:uppercase}
.news-date{font-size:12px;color:var(--pink);margin-top:10px;text-transform:uppercase}
.news-body{font-size:10px;color:#ddd;margin-top:12px;line-height:1.55;text-transform:uppercase;width:390px}
.news-more{width:22px;height:22px;border:1px solid var(--pink);margin-top:10px;display:flex;align-items:center;justify-content:center}

/* testimonials */
.arrows{left:83px;top:2157px;display:flex;gap:4px}
.arrows span{width:26px;height:26px;background:#e6e6e6;display:flex;align-items:center;justify-content:center}
.person{width:260px;text-align:center}
.avatar{width:104px;height:104px;border-radius:50%;margin:0 auto;border:3px solid #eee}
.person h3{font-size:16px;font-weight:500;color:#222;margin-top:14px;text-transform:uppercase}
.person p{font-size:10px;color:#555;line-height:1.5;margin-top:16px;text-align:left;padding:0 18px}
.divider{width:1px;height:228px;background:#ccc;top:2178px}

/* partners */
.partners{left:0;top:2470px;width:996px;height:92px;background:#f2f2f2;display:flex;align-items:center;justify-content:space-around;padding:0 60px}
.partners span{width:120px;height:22px;background:#9a9a9a;border-radius:3px}

/* newsletter */
.newsletter{left:0;top:2572px;width:996px;height:115px;background:var(--band)}
.nl-label{left:156px;top:38px;font-size:18px;color:#e8e8e8;font-weight:300}
.nl-input{left:521px;top:38px;width:270px;height:27px;background:#fff;font-size:11px;color:#888;padding:7px 8px}
.nl-btn{left:812px;top:38px;width:123px;height:27px;background:var(--pink);color:#fff;font-size:11px;display:flex;align-items:center;justify-content:center}

/* footer */
.footer{left:0;top:2687px;width:996px;height:302px;background:var(--dark)}
.foot-h{font-size:15px;color:#e8e8e8;text-transform:uppercase;letter-spacing:.5px}
.foot-list{list-style:none;margin-top:16px}
.foot-list li{font-size:9.5px;color:#cfcfcf;text-transform:uppercase;line-height:20.8px;padding-left:14px}
.cards{display:flex;gap:6px;margin-top:16px}
.cards span{width:34px;height:20px;border-radius:2px;background:#3d63b7}
.cards span:nth-child(2){background:#e7e7e7}
.cards span:nth-child(3){background:#d9534f}
.cards span:nth-child(4){background:#4a86c8}
.social{display:flex;gap:7px;margin-top:16px}
.social span{width:24px;height:24px;border-radius:50%;background:#3b5fa8}
.social span:nth-child(2){background:#2aa5e0}
.social span:nth-child(3){background:#d24a3b}
.social span:nth-child(4){background:#4a7aa6;border-radius:4px}
.copyright{right:60px;top:262px;font-size:9.5px;color:#cfcfcf;text-transform:uppercase}
</style>
</head>
<body>
<div class="page">

  <div class="abs topbar">
    <div class="pay-mini"><span></span><span></span><span></span><span></span><span></span></div>
    <div class="account"><span>Login</span><span>Register</span><span>Wish list</span></div>
  </div>

  <header class="abs header">
    <div class="abs phone">
      <span class="phone-ico"><svg width="12" height="12" viewBox="0 0 24 24"><path fill="#fff" d="M6.6 10.8a15 15 0 0 0 6.6 6.6l2.2-2.2c.3-.3.7-.4 1-.2 1.1.4 2.3.6 3.6.6.6 0 1 .4 1 1V20c0 .6-.4 1-1 1A17 17 0 0 1 3 4c0-.6.4-1 1-1h3.5c.6 0 1 .4 1 1 0 1.3.2 2.5.6 3.6.1.3 0 .7-.2 1z"/></svg></span>
      0161 555 0199
    </div>
    <div class="abs brand">Tavren</div>
    <div class="abs cart"><svg width="26" height="24" viewBox="0 0 26 24"><path d="M2 3h4l3 12h12l3-9H8" fill="none" stroke="#fff" stroke-width="2"/><circle cx="11" cy="20" r="2" fill="#fff"/><circle cx="19" cy="20" r="2" fill="#fff"/></svg></div>
    <div class="abs cart-count">0</div>
  </header>

  <nav class="abs nav">
    <a class="active" href="#">Home</a><a href="#">About us</a><a href="#">Products ↓</a><a href="#">Artwork guidelines ↓</a><a href="#">How to order</a><a href="#">News</a><a href="#">Contact us</a>
  </nav>
  <svg class="abs search" width="20" height="20" viewBox="0 0 20 20"><circle cx="8" cy="8" r="6" fill="none" stroke="#f07aa0" stroke-width="2.4"/><path d="M12.5 12.5l6 6" stroke="#f07aa0" stroke-width="2.6"/></svg>

  <div class="abs hero" role="img" aria-label="Four young girls in stylish coats and dresses seated on a white sofa"></div>

  <h2 class="abs section-title" style="top:538px">Our Product</h2>
  <div class="abs rule" style="left:270px;top:591px;width:456px"></div>

  <!-- products row 1 -->
  <div class="abs card shop" style="left:75px;top:645px">
    <div class="photo" role="img" aria-label="Two children in winter jackets" style="background:linear-gradient(135deg,#8a7f79,#b9aca3)"></div>
    <div class="shop-label">SHOP</div>
    <div class="caption">Product name<div class="price">From $49.00</div><span class="arrow"><svg width="10" height="10" viewBox="0 0 10 10"><path d="M3 1l4 4-4 4" fill="none" stroke="#fff" stroke-width="1.6"/></svg></span></div>
  </div>
  <div class="abs card" style="left:294px;top:645px">
    <div class="photo" role="img" aria-label="Girl in a white coat and pink skirt" style="background:linear-gradient(135deg,#c9c9c9,#eaeaea)"></div>
    <div class="caption">Product name<div class="price">From $59.00</div></div>
  </div>
  <div class="abs card" style="left:510px;top:645px">
    <div class="photo" role="img" aria-label="Girl in a camel cape coat" style="background:linear-gradient(135deg,#b9a58f,#d8c8b3)"></div>
    <div class="caption">Product name<div class="price">From $99.00</div></div>
  </div>
  <div class="abs card" style="left:727px;top:645px">
    <div class="photo" role="img" aria-label="Toddler girl in a beige peacoat" style="background:linear-gradient(135deg,#e2ddd6,#f4f1ec)"></div>
    <div class="caption">Product name<div class="price">From $129.00</div></div>
  </div>

  <!-- products row 2 -->
  <div class="abs card" style="left:75px;top:900px">
    <div class="photo" role="img" aria-label="Toddler in a knitted cream cardigan" style="background:linear-gradient(135deg,#e8e4de,#f6f3ef)"></div>
    <div class="caption">Product name<div class="price">From $49.00</div></div>
  </div>
  <div class="abs card" style="left:294px;top:900px">
    <div class="photo" role="img" aria-label="Two girls in trench coats" style="background:linear-gradient(135deg,#b89e8c,#e2d6cc)"></div>
    <div class="caption">Product name<div class="price">From $59.00</div></div>
  </div>
  <div class="abs card" style="left:510px;top:900px">
    <div class="photo" role="img" aria-label="Two girls in patterned coats" style="background:linear-gradient(135deg,#9d7f74,#d6c4bb)"></div>
    <div class="caption">Product name<div class="price">From $99.00</div></div>
  </div>
  <div class="abs card" style="left:727px;top:900px">
    <div class="photo" role="img" aria-label="Little boy in a navy padded jacket" style="background:linear-gradient(135deg,#d5d8dd,#f1f2f4)"></div>
    <div class="caption">Product name<div class="price">From $129.00</div></div>
  </div>

  <!-- promos -->
  <div class="abs promo-left" role="img" aria-label="Three children in colourful winter coats">
    <div class="offer">GREAT OFFERS<br>FOR YOU<b>GRAB IT</b></div>
  </div>
  <div class="abs promo-center" role="img" aria-label="Three girls in animal-print dresses"><span>PRODUCT NAME</span></div>
  <div class="abs promo-r1" role="img" aria-label="Group of teens in dark outerwear"></div>
  <div class="abs promo-r2" role="img" aria-label="Children playing on a beach"></div>

  <!-- news -->
  <section class="abs news" role="img" aria-label="Children running with balloons, darkened backdrop"></section>
  <h2 class="abs section-title news-title" style="top:1474px">Latest News</h2>
  <div class="abs rule" style="left:270px;top:1527px;width:456px;background:#8a8a8a"></div>

  <div class="abs" style="left:125px;top:1566px;width:333px;height:221px;border:2px solid #fff"></div>
  <div class="abs frame" style="left:145px;top:1584px;width:333px;height:203px" role="img" aria-label="Collage of toddlers in colourful outfits"><div style="width:100%;height:100%;background:linear-gradient(135deg,#c9b8a3,#e6e0da 50%,#a5b7c8)"></div></div>

  <div class="abs" style="left:537px;top:1604px">
    <div class="news-h">Making a great business card</div>
    <div class="news-date">4th Jun 2015</div>
    <div class="news-body">A business card is an integral part of any good marketing plan. For its size and cost, it's probably the most powerful part. Of course, you can't expect your business card to tell the whole story... See more at: tavrenimports.com/news</div>
    <div class="news-more"><svg width="10" height="10" viewBox="0 0 10 10"><path d="M3 1l4 4-4 4" fill="none" stroke="#e8457a" stroke-width="1.6"/></svg></div>
  </div>

  <div class="abs" style="left:127px;top:1851px">
    <div class="news-h">Welcome to our new website</div>
    <div class="news-date">21st May 2015</div>
    <div class="news-body" style="width:200px">News coming soon...</div>
    <div class="news-more"><svg width="10" height="10" viewBox="0 0 10 10"><path d="M3 1l4 4-4 4" fill="none" stroke="#e8457a" stroke-width="1.6"/></svg></div>
  </div>

  <div class="abs" style="left:570px;top:1777px;width:334px;height:208px;border:2px solid #fff"></div>
  <div class="abs frame" style="left:550px;top:1795px;width:334px;height:190px" role="img" aria-label="Two children posing with a vintage motorcycle"><div style="width:100%;height:100%;background:linear-gradient(135deg,#8a8580,#c9c3bc 50%,#6d6964)"></div></div>

  <!-- testimonials -->
  <h2 class="abs section-title" style="top:2066px">Testimonial</h2>
  <div class="abs rule" style="left:270px;top:2113px;width:456px"></div>
  <div class="abs arrows">
    <span><svg width="8" height="10" viewBox="0 0 8 10"><path d="M6 1L2 5l4 4" fill="none" stroke="#555" stroke-width="1.5"/></svg></span>
    <span><svg width="8" height="10" viewBox="0 0 8 10"><path d="M2 1l4 4-4 4" fill="none" stroke="#555" stroke-width="1.5"/></svg></span>
  </div>

  <div class="abs person" style="left:76px;top:2177px">
    <div class="avatar" role="img" aria-label="Portrait of Jhone Doe" style="background:linear-gradient(135deg,#6e5a4c,#b39b88)"></div>
    <h3>Jhone Doe</h3>
    <p>Lorem Ipsum is simply dummy text of the printing and typesetting industry. Lorem Ipsum has been the industry's standard dummy text ever since the 1500s, when an unknown printer took.</p>
  </div>
  <div class="abs divider" style="left:354px"></div>
  <div class="abs person" style="left:378px;top:2177px">
    <div class="avatar" role="img" aria-label="Portrait of Stela Smith" style="background:linear-gradient(135deg,#5a4438,#c8a893)"></div>
    <h3>Stela Smith</h3>
    <p>Lorem Ipsum is simply dummy text of the printing and typesetting industry. Lorem Ipsum has been the industry's standard dummy text ever since the 1500s, when an unknown printer took.</p>
  </div>
  <div class="abs divider" style="left:650px"></div>
  <div class="abs person" style="left:659px;top:2177px">
    <div class="avatar" role="img" aria-label="Portrait of Mark Joe" style="background:linear-gradient(135deg,#7b7f86,#d1d3d6)"></div>
    <h3>Mark Joe</h3>
    <p>Lorem Ipsum is simply dummy text of the printing and typesetting industry. Lorem Ipsum has been the industry's standard dummy text ever since the 1500s, when an unknown printer took.</p>
  </div>

  <!-- partners -->
  <div class="abs partners"><span></span><span></span><span></span><span></span><span></span></div>

  <!-- newsletter -->
  <div class="abs newsletter">
    <svg class="abs" style="left:80px;top:38px" width="38" height="28" viewBox="0 0 38 28"><rect x="1.5" y="1.5" width="35" height="25" fill="none" stroke="#e8457a" stroke-width="2.4"/><path d="M2 3l17 13L36 3" fill="none" stroke="#e8457a" stroke-width="2.4"/></svg>
    <div class="abs nl-label">Sign Up for Our Newsletter:</div>
    <div class="abs nl-input">Enter your e-mail</div>
    <div class="abs nl-btn">OK</div>
  </div>

  <!-- footer -->
  <footer class="abs footer">
    <div class="abs" style="left:60px;top:39px">
      <div class="foot-h">Quick links</div>
      <ul class="foot-list">
        <li>Business cards</li><li>Compliment slips</li><li>Letterheads</li><li>Envelopes</li><li>Presentation folders</li><li>Large posters</li><li>Banners</li><li>Flyers</li><li>Leaflets (folded)</li><li>Brochures/booklets - stapled</li>
      </ul>
    </div>
    <div class="abs" style="left:329px;top:39px">
      <div class="foot-h">Information</div>
      <ul class="foot-list">
        <li>Home</li><li>About us</li><li>Artwork guidelines</li><li>How to order</li><li>Contact us</li><li>Small print</li><li>Privacy policy</li><li>Terms &amp; conditions</li><li>Delivery information</li>
      </ul>
    </div>
    <div class="abs" style="left:544px;top:39px">
      <div class="foot-h">We accept</div>
      <div class="cards"><span></span><span></span><span></span><span></span><span></span><span></span><span></span></div>
      <div class="foot-h" style="margin-top:34px">Connect with us</div>
      <div class="social"><span></span><span></span><span></span><span></span></div>
    </div>
    <div class="abs copyright">© Tavren 2017</div>
  </footer>

</div>
</body>
</html>
```